Tressel Linkworks Line Card

Hello - We're looking to develop a two sided brochure for our company product lines and capabilities. We're a distributor, value-added reseller, we build cable assemblies and panel assemblies. Looking for a flyer to help tell our story. Our primary market is selling to customers in the off-highway equipment markets. Construction, AG and Specialty Vehicles.

```html
<!DOCTYPE html>
<html lang="en">
<head>
<meta charset="utf-8">
<title>Tressel Linkworks Line Card</title>
<link href="https://fonts.googleapis.com/css2?family=Poppins:wght@400;500;600;700;800&display=swap" rel="stylesheet">
<style>
:root{
  --navy:#232b4f;
  --red:#ee1c25;
  --white:#ffffff;
  --ink:#141414;
  --stage:#e8e8ea;
}
*{margin:0;padding:0;box-sizing:border-box}
html,body{width:882px;height:1200px;overflow:hidden}
body{background:var(--stage);font-family:'Poppins',sans-serif;color:var(--ink);position:relative}
.page{position:absolute;top:315px;width:420px;height:570px;background:var(--white);overflow:hidden;box-shadow:0 4px 14px rgba(0,0,0,.12)}
.page--front{left:14px}
.page--back{left:448px}
.page svg.bg{position:absolute;inset:0;width:420px;height:570px}
.abs{position:absolute}

.brand-name{font-weight:800;color:var(--navy);font-size:17px;line-height:1;letter-spacing:-.5px;display:flex;align-items:center;gap:6px;white-space:nowrap}
.brand-name .mark{width:9px;height:9px;background:var(--red)}
.brand-bar{height:13px;background:var(--navy);color:var(--white);font-weight:700;font-size:8px;line-height:13px;text-align:right;padding-right:8px;white-space:nowrap}
.tagline{font-weight:700;font-size:9px;line-height:11.5px;text-align:right;white-space:nowrap}
.tagline .accent{color:var(--red)}

.address{left:294px;top:0;width:126px;height:24px;background:var(--navy);color:var(--white);border-radius:0 0 0 10px;font-weight:700;font-size:7.6px;line-height:9.5px;text-align:center;padding-top:2px}
.phone{left:294px;top:26px;width:126px;text-align:center;color:var(--red);font-weight:700;font-size:10px}
.fax{left:294px;top:40px;width:126px;text-align:center;font-weight:600;font-size:8px}

.list{list-style:none;font-size:9.6px;line-height:14px}
.list li{position:relative;padding-left:9px;white-space:nowrap}
.list li::before{content:"";position:absolute;left:0;top:4.5px;width:5.5px;height:5.5px;border-radius:50%;background:var(--red);box-shadow:inset 0 0 0 1px rgba(255,255,255,.5)}
.list--light{color:var(--white)}
.list--navydot li::before{background:var(--navy)}

.partners{display:grid;grid-template-columns:auto auto;gap:6px 10px;align-items:center;justify-items:start;font-weight:700;color:var(--navy)}
.partner{font-size:9.5px;line-height:1;white-space:nowrap}
.partner--wide{grid-column:1 / span 2;justify-self:end;font-size:11.5px;letter-spacing:.6px}
.partner small{display:block;font-size:4px;font-weight:700;letter-spacing:.3px;margin-top:1px}

.web-front{left:120px;width:300px;top:550px;text-align:center;color:var(--white);font-size:10px}
.contact-back{left:0;width:420px;top:528px;text-align:center;font-weight:700;font-size:9.5px;color:var(--navy)}
.contact-back .fax-inline{font-size:8px}
.web-back{left:0;width:420px;top:544px;text-align:center;font-weight:700;font-size:10px;letter-spacing:3.2px;color:var(--ink)}
</style>
</head>
<body>

<section class="page page--front">
  <svg class="bg" viewBox="0 0 420 570" xmlns="http://www.w3.org/2000/svg">
    <defs>
      <linearGradient id="productTone" x1="0" y1="0" x2="1" y2="1">
        <stop offset="0" stop-color="#f2f2f2"/>
        <stop offset=".45" stop-color="#1d1d20"/>
        <stop offset="1" stop-color="#9aa3ad"/>
      </linearGradient>
      <linearGradient id="cableTone" x1="0" y1="0" x2="1" y2="0">
        <stop offset="0" stop-color="#e07a3a"/>
        <stop offset=".5" stop-color="#b58ad0"/>
        <stop offset="1" stop-color="#6f7c8a"/>
      </linearGradient>
    </defs>
    <path d="M0,232 C70,222 150,225 205,165 C240,130 300,124 420,120 L420,440 L0,440 Z" fill="var(--red)"/>
    <path d="M0,320 C70,302 160,312 230,330 L420,330 L420,570 L0,570 Z" fill="var(--navy)"/>
    <circle cx="335" cy="290" r="170" fill="var(--white)"/>
    <path d="M110,570 C180,520 260,480 420,452 L420,570 Z" fill="var(--white)"/>
    <path d="M120,570 C170,535 230,520 420,508 L420,570 Z" fill="var(--red)"/>

    <polygon points="243,2 278,20 278,60 243,78 208,60 208,20" fill="var(--navy)"/>
    <polygon role="img" aria-label="Photo of a row of multicoloured wire harness connectors" points="243,8 272,23 272,57 243,72 214,57 214,23" fill="url(#cableTone)"/>

    <rect role="img" aria-label="Photo of three rotary selector switches" x="285" y="92" width="128" height="50" rx="6" fill="#b9a98e"/>
    <rect role="img" aria-label="Photo of a rotary battery disconnect switch with key" x="230" y="170" width="170" height="270" rx="40" fill="url(#productTone)"/>

    <g>
      <polygon points="41,519 60,530 60,552 41,563 22,552 22,530" fill="var(--red)"/>
      <polygon role="img" aria-label="Photo of a battery isolator switch" points="41,523 56,532 56,550 41,559 26,550 26,532" fill="#c8653a"/>
      <polygon points="104,514 123,525 123,547 104,558 85,547 85,525" fill="var(--red)"/>
      <polygon role="img" aria-label="Photo of an operator display panel" points="104,518 119,527 119,545 104,554 89,545 89,527" fill="#7a7f88"/>
      <polygon points="161,488 180,499 180,521 161,532 142,521 142,499" fill="var(--red)"/>
      <polygon role="img" aria-label="Photo of green terminal block connectors" points="161,492 176,501 176,519 161,528 146,519 146,501" fill="#4f9a4a"/>
      <polygon points="218,456 237,467 237,489 218,500 199,489 199,467" fill="var(--red)"/>
      <polygon role="img" aria-label="Photo of loose wire leads" points="218,460 233,469 233,487 218,496 203,487 203,469" fill="#b8b0a6"/>
      <polygon points="275,430 294,441 294,463 275,474 256,463 256,441" fill="var(--red)"/>
      <polygon role="img" aria-label="Photo of an enclosure with selector switch" points="275,434 290,443 290,461 275,470 260,461 260,443" fill="#9a9aa0"/>
    </g>
  </svg>

  <div class="abs" style="left:15px;top:34px;">
    <div class="brand-name"><span class="mark"></span>Tressel Linkworks</div>
  </div>
  <div class="abs brand-bar" style="left:15px;top:55px;width:180px;">Tressel Linkworks, Inc.</div>
  <p class="abs tagline" style="left:10px;top:72px;width:180px;">Distribution, Contract Manufacturing,<br><span class="accent">and System Integration</span></p>

  <p class="abs address">4120 HARROW RIDGE BLVD.<br>ELMWOOD, IL 60431</p>
  <p class="abs phone">(555)014-2270</p>
  <p class="abs fax">FAX : (555) 014-2276</p>

  <ul class="abs list" style="left:20px;top:111px;">
    <li>Power Distribution Modules</li>
    <li>Circuit Breakers, Fuses</li>
    <li>rocker &amp; Toggle Switches</li>
    <li>CAN Switches</li>
    <li>Battery Disconnects</li>
    <li>Battery Equalizers</li>
    <li>Power Converters</li>
    <li>True Sine Wave Inverters</li>
  </ul>

  <ul class="abs list list--light list--navydot" style="left:20px;top:252px;">
    <li>Battery Separators</li>
    <li>Interconnect Controllers</li>
    <li>Battery Isolators</li>
  </ul>

  <ul class="abs list list--light" style="left:20px;top:334px;">
    <li>On Vehicle &amp; Mobile</li>
    <li>Equipment Display</li>
    <li>HMIs Displays SCADA Software</li>
    <li>HMI + PLC Hybrids</li>
    <li>Automation Cables Connectors</li>
    <li>Passive Distributors</li>
    <li>DIN Valve Connectors</li>
    <li>Industrial Ethernet/Connectors</li>
    <li>Fuse Blocks , Fuse Holders</li>
    <li>Circuit Breakers</li>
    <li>Resettable Fuses</li>
    <li>Fuse Accessories</li>
  </ul>

  <div class="abs partners" style="right:12px;top:474px;">
    <span class="partner partner--wide">VANTRELL</span>
    <span class="partner">KORVANE</span>
    <span class="partner">FUSEMARK</span>
    <span class="partner">DALVEX</span>
    <span class="partner">Brightel Systems<small>A HOLLIN BRAND</small></span>
  </div>

  <p class="abs web-front">www.tresselworks.com</p>
</section>

<section class="page page--back">
  <svg class="bg" viewBox="0 0 420 570" xmlns="http://www.w3.org/2000/svg">
    <rect x="0" y="117" width="420" height="400" fill="var(--navy)"/>
    <rect x="49" y="112" width="322" height="6" rx="3" fill="var(--red)"/>
    <rect x="49" y="514" width="322" height="6" rx="3" fill="var(--red)"/>

    <g>
      <rect role="img" aria-label="Photo of bolted power distribution block with red cover" x="29" y="139" width="110" height="104" rx="10" fill="#8d8a86"/>
      <rect role="img" aria-label="Photo of wired control module in a blue frame" x="156" y="139" width="110" height="104" rx="10" fill="#4d5670"/>
      <rect role="img" aria-label="Photo of a terminal strip inside an enclosure" x="283" y="139" width="110" height="104" rx="10" fill="#b7b6b1"/>
      <rect x="163" y="250" width="95" height="4" rx="2" fill="var(--white)"/>

      <rect role="img" aria-label="Photo of a fuse holder rail with red caps" x="29" y="261" width="110" height="104" rx="10" fill="#a39a8d"/>
      <rect role="img" aria-label="Photo of a wire harness laid out on a build board" x="156" y="261" width="110" height="104" rx="10" fill="#b5a58c"/>
      <rect role="img" aria-label="Photo of a sealed junction box with cables" x="283" y="261" width="110" height="104" rx="10" fill="#6c6f75"/>
      <rect x="36" y="372" width="95" height="4" rx="2" fill="var(--white)"/>
      <rect x="163" y="372" width="95" height="4" rx="2" fill="var(--white)"/>
      <rect x="290" y="372" width="95" height="4" rx="2" fill="var(--white)"/>

      <rect role="img" aria-label="Photo of a wired control panel with relays" x="29" y="381" width="110" height="104" rx="10" fill="#8f9196"/>
      <rect role="img" aria-label="Photo of terminal blocks with yellow ferrules" x="156" y="381" width="110" height="104" rx="10" fill="#7b7665"/>
      <rect role="img" aria-label="Photo of red wire bundle routed in a panel" x="283" y="381" width="110" height="104" rx="10" fill="#5a4d50"/>
      <rect x="163" y="492" width="95" height="4" rx="2" fill="var(--white)"/>
    </g>
  </svg>

  <div class="abs" style="left:18px;top:46px;">
    <div class="brand-name"><span class="mark"></span>Tressel Linkworks</div>
  </div>
  <div class="abs brand-bar" style="left:18px;top:67px;width:176px;">Tressel Linkworks, Inc.</div>
  <p class="abs tagline" style="left:14px;top:84px;width:180px;">Distribution, Contract Manufacturing,<br><span class="accent">and System Integration</span></p>

  <div class="abs partners" style="right:14px;top:28px;">
    <span class="partner partner--wide">VANTRELL</span>
    <span class="partner">KORVANE</span>
    <span class="partner">FUSEMARK</span>
    <span class="partner">DALVEX</span>
    <span class="partner">Brightel Systems<small>A HOLLIN BRAND</small></span>
  </div>

  <p class="abs contact-back">(555)014-2270 <span class="fax-inline">FAX : (555) 014-2276</span></p>
  <p class="abs web-back">www.tresselworks.com</p>
</section>

</body>
</html>
```